MORVEK IT Limited Buisness card logo

I am setting up a IT Consultancy company and want a logo that is related to the IT industry, but also i am thinking that the A in MOR and the A in VEK are linked together maybe horizontally and vertically, also thought about the A being @ as it symbolises IT services. This logo will be used on paperwork, business cards and website.

Industry/Entity Type

Business

Contact Information for Business Card

Gareth Wilmslow
MORVEK IT Limited
IT Consultant
Mobile: 07912563084
Email: garethwk@fernmail.co.uk

Requirements
Must have
• IT Theme

```html
<!DOCTYPE html>
<html lang="en">
<head>
<meta charset="utf-8">
<title>MORVEK IT Limited – Business Card</title>
<link rel="stylesheet" href="https://fonts.googleapis.com/css2?family=Josefin+Sans:wght@300;400&display=swap">
<style>
  :root {
    --backdrop: #d8d3cb;
    --card: #141414;
    --card-edge: #0a0a0a;
    --ink: #f2f2f2;
    --ink-soft: #bdbdbd;
    --accent: #6cc04a;
    --rule: #8a8a8a;
    --ghost: #262626;
  }
  * { box-sizing: border-box; margin: 0; padding: 0; }
  html, body { width: 1200px; height: 1000px; overflow: hidden; }
  body {
    background: var(--backdrop);
    display: flex;
    align-items: center;
    justify-content: center;
  }
  .card {
    position: relative;
    width: 860px;
    height: 500px;
    background: linear-gradient(135deg, #1c1c1c 0%, var(--card) 55%, var(--card-edge) 100%);
    border-radius: 6px;
    box-shadow: 0 18px 40px rgba(0,0,0,0.35);
    overflow: hidden;
    font-family: "Josefin Sans", sans-serif;
    color: var(--ink);
  }
  .ghost-name {
    position: absolute;
    right: 40px;
    top: 170px;
    font-weight: 300;
    font-size: 104px;
    line-height: 1;
    letter-spacing: 2px;
    color: var(--ghost);
    white-space: nowrap;
  }
  .brand {
    position: absolute;
    left: 40px;
    top: 52px;
    display: flex;
    align-items: center;
    gap: 10px;
  }
  .brand__name {
    font-weight: 300;
    font-size: 28px;
    line-height: 1;
    letter-spacing: 1px;
    color: var(--ink);
  }
  .brand__dot {
    width: 20px;
    height: 20px;
    border: 2px solid var(--accent);
    border-radius: 50%;
  }
  .headline {
    position: absolute;
    left: 250px;
    top: 46px;
    width: 570px;
  }
  .headline__title {
    font-weight: 300;
    font-size: 38px;
    line-height: 1.1;
    letter-spacing: 1px;
    white-space: nowrap;
  }
  .headline__title .accent { color: var(--accent); }
  .headline__rule {
    margin-top: 10px;
    height: 1px;
    background: var(--rule);
  }
  .headline__role {
    margin-top: 10px;
    text-align: right;
    font-weight: 300;
    font-size: 18px;
    letter-spacing: 5px;
    color: var(--ink-soft);
  }
  .contact {
    position: absolute;
    left: 60px;
    bottom: 56px;
  }
  .contact__name {
    font-weight: 400;
    font-size: 28px;
    letter-spacing: 1.5px;
    text-transform: uppercase;
    margin-bottom: 18px;
  }
  .contact__line {
    display: flex;
    align-items: center;
    gap: 12px;
    font-weight: 300;
    font-size: 22px;
    letter-spacing: 1px;
    margin-top: 10px;
  }
  .contact__icon { width: 24px; height: 24px; flex: none; }
</style>
</head>
<body>
  <article class="card">
    <div class="ghost-name" aria-hidden="true">MORVEK</div>

    <div class="brand">
      <span class="brand__name">MORVEK</span>
      <span class="brand__dot"></span>
    </div>

    <header class="headline">
      <h1 class="headline__title">MOR<span class="accent">VEK</span> IT Limited IT</h1>
      <div class="headline__rule"></div>
      <p class="headline__role">Consultant</p>
    </header>

    <section class="contact">
      <h2 class="contact__name">Gareth Wilmslow</h2>
      <p class="contact__line">
        <svg class="contact__icon" viewBox="0 0 24 24" aria-hidden="true">
          <circle cx="12" cy="12" r="12" fill="#6cc04a"/>
          <rect x="8" y="5.5" width="8" height="13" rx="1.5" fill="none" stroke="#141414" stroke-width="1.6"/>
          <line x1="10.5" y1="16" x2="13.5" y2="16" stroke="#141414" stroke-width="1.4"/>
        </svg>
        07 91 256 3084
      </p>
      <p class="contact__line">
        <svg class="contact__icon" viewBox="0 0 24 24" aria-hidden="true">
          <circle cx="12" cy="12" r="12" fill="#6cc04a"/>
          <rect x="6" y="8" width="12" height="8.5" rx="1" fill="none" stroke="#141414" stroke-width="1.6"/>
          <polyline points="6,8.5 12,13 18,8.5" fill="none" stroke="#141414" stroke-width="1.6"/>
        </svg>
        garethwk@fernmail.co.uk
      </p>
    </section>
  </article>
</body>
</html>
```